Playing Card Box Deisgn

Quick video of what we're looking for in this design:

https://share.clipnook.com/watch/r2KTP48mdqHxzbnu7LWyPe?

Here's our company website:
https://mybrambletoys.com/

Attached is the file of what we have so far for this box design. Feel free to add or make other design suggestions

```html
<!DOCTYPE html>
<html lang="en">
<head>
<meta charset="utf-8">
<title>Brambletoys Playing Cards – Box Dieline</title>
<link rel="stylesheet" href="https://fonts.googleapis.com/css2?family=Jost:ital,wght@0,500;0,600;1,400&family=Montserrat:wght@700&family=Playfair+Display:wght@700&family=Cormorant+Garamond:wght@500;600&display=swap">
<style>
  :root {
    --page: #ffffff;
    --board: #231f20;
    --cut-line: #d77fb0;
    --frame: #f0822d;
    --ink-light: #ffffff;
    --ink-dark: #231f20;
    --heart: #e5312f;
    --club: #7bb843;
    --diamond: #f6b92b;
    --spade: #5a63b0;
  }
  html, body {
    margin: 0;
    padding: 0;
    width: 848px;
    height: 1200px;
    overflow: hidden;
    background: var(--page);
  }
  .canvas {
    position: relative;
    width: 848px;
    height: 1200px;
  }
  .dieline {
    position: absolute;
    left: 0;
    top: 0;
    width: 848px;
    height: 1200px;
  }
  .board { fill: var(--board); }
  .cut { fill: none; stroke: var(--cut-line); stroke-width: 1.4; }
  .frame { fill: none; stroke: var(--frame); stroke-width: 4; }
  .frame-thin { fill: none; stroke: var(--frame); stroke-width: 2; }
  .frame-dotted { fill: none; stroke: var(--frame); stroke-width: 2; stroke-dasharray: 2 5; }
  .brand-title {
    font-family: "Playfair Display", Georgia, serif;
    font-weight: 700;
    font-size: 66px;
    fill: var(--ink-light);
  }
  .product-line {
    font-family: "Montserrat", Arial, sans-serif;
    font-weight: 700;
    font-size: 31px;
    letter-spacing: -2px;
    fill: var(--ink-light);
  }
  .edition-pill { fill: var(--frame); }
  .edition-label {
    font-family: "Cormorant Garamond", Georgia, serif;
    font-weight: 600;
    font-size: 19px;
    fill: var(--ink-dark);
  }
  .back-brand {
    font-family: "Cormorant Garamond", Georgia, serif;
    font-weight: 500;
    font-size: 17px;
    letter-spacing: 9px;
    fill: var(--ink-light);
  }
  .back-copy {
    font-family: "Jost", Arial, sans-serif;
    font-style: italic;
    font-weight: 400;
    font-size: 14.5px;
    fill: var(--ink-light);
  }
  .web-address {
    font-family: "Jost", Arial, sans-serif;
    font-weight: 600;
    font-size: 10.5px;
    letter-spacing: 2px;
    fill: var(--ink-light);
  }
  .side-address {
    font-family: "Jost", Arial, sans-serif;
    font-weight: 600;
    font-size: 14px;
    letter-spacing: 2.5px;
    fill: var(--ink-light);
  }
  .suit { font-family: "Jost", Arial, sans-serif; font-size: 20px; }
  .suit-heart { fill: var(--heart); }
  .suit-club { fill: var(--club); }
  .suit-diamond { fill: var(--diamond); }
  .suit-spade { fill: var(--spade); }
  .pip { fill: var(--frame); }
  .badge-disc { fill: var(--board); }
  .badge-name {
    font-family: "Jost", Arial, sans-serif;
    font-weight: 500;
    font-size: 17px;
    fill: var(--ink-light);
  }
</style>
</head>
<body>
<main class="canvas">
  <svg class="dieline" viewBox="0 0 1623 2297" xmlns="http://www.w3.org/2000/svg">
    <defs>
      <radialGradient id="emblem-tones" cx="50%" cy="50%" r="60%">
        <stop offset="0%" stop-color="#3b3340"/>
        <stop offset="55%" stop-color="#4a3a3a"/>
        <stop offset="100%" stop-color="#2b2527"/>
      </radialGradient>
    </defs>

    <!-- printed sheet -->
    <rect class="board" x="256" y="37" width="1066" height="940"/>

    <!-- cut & fold lines -->
    <g class="cut-lines">
      <path class="cut" d="M436,263 L436,135 Q436,62 612,62 Q789,62 789,135 L789,263"/>
      <line class="cut" x1="436" y1="165" x2="789" y2="165"/>
      <path class="cut" d="M436,263 L337,263 L337,181 L410,181 L420,228 L436,246"/>
      <path class="cut" d="M789,263 L887,263 L887,181 L814,181 L804,228 L789,246"/>
      <rect class="cut" x="337" y="263" width="99" height="488"/>
      <rect class="cut" x="436" y="263" width="353" height="488"/>
      <rect class="cut" x="789" y="263" width="98" height="488"/>
      <rect class="cut" x="887" y="263" width="353" height="488"/>
      <path class="cut" d="M1240,263 L1314,290 L1314,727 L1240,751"/>
      <path class="cut" d="M337,751 L337,833 L410,833 L420,785 L436,768"/>
      <path class="cut" d="M887,751 L887,833 L814,833 L804,785 L789,768"/>
      <path class="cut" d="M887,751 L887,875 Q887,950 1063,950 Q1240,950 1240,875 L1240,751"/>
      <line class="cut" x1="887" y1="850" x2="1240" y2="850"/>
    </g>

    <!-- top end panel -->
    <g class="top-end">
      <rect class="frame" x="449" y="177" width="327" height="72"/>
      <path class="frame-thin" d="M468,187 L757,187 L767,197 L767,229 L757,239 L468,239 L458,229 L458,197 Z"/>
      <text class="pip" x="492" y="219" font-size="14" text-anchor="middle">◆</text>
      <text class="suit suit-heart" x="545" y="220" text-anchor="middle">♥</text>
      <text class="suit suit-club" x="590" y="220" text-anchor="middle">♣</text>
      <text class="suit suit-diamond" x="635" y="220" text-anchor="middle">♦</text>
      <text class="suit suit-spade" x="680" y="220" text-anchor="middle">♠</text>
      <text class="pip" x="733" y="219" font-size="14" text-anchor="middle">◆</text>
    </g>

    <!-- front panel -->
    <g class="front-panel">
      <rect class="frame" x="449" y="279" width="327" height="463"/>
      <rect class="frame-dotted" x="461" y="290" width="303" height="441"/>
      <text class="brand-title" x="612" y="392" text-anchor="middle" textLength="258" lengthAdjust="spacingAndGlyphs">BRAMBLETOYS</text>
      <path class="frame" d="M530,411 L695,411 L722,438 L722,609 L695,636 L530,636 L503,609 L503,438 Z"/>
      <path d="M533,418 L692,418 L715,441 L715,606 L692,629 L533,629 L510,606 L510,441 Z" fill="url(#emblem-tones)" role="img" aria-label="Emblem of the four card suits in colour, crossed by two white lines"/>
      <text class="product-line" x="612" y="700" text-anchor="middle">PLAYING CARDS</text>
      <rect class="edition-pill" x="553" y="720" width="118" height="25" rx="12.5"/>
      <text class="edition-label" x="612" y="739" text-anchor="middle">STANDARD</text>
    </g>

    <!-- left side panel -->
    <g class="side-panel">
      <rect class="frame-thin" x="355" y="280" width="65" height="455"/>
      <text class="side-address" transform="translate(381,508) rotate(90)" text-anchor="middle">WWW.MYBRAMBLETOYS.COM</text>
    </g>

    <!-- right side panel -->
    <g class="side-panel">
      <rect class="frame-thin" x="806" y="280" width="65" height="455"/>
      <text class="side-address" transform="translate(843,508) rotate(-90)" text-anchor="middle">WWW.MYBRAMBLETOYS.COM</text>
    </g>

    <!-- back panel -->
    <g class="back-panel">
      <path class="frame" d="M901,279 L1003,279 A60,34 0 0 0 1123,279 L1225,279 L1225,741 L901,741 Z"/>
      <rect class="frame-thin" x="912" y="290" width="303" height="440"/>
      <text class="back-brand" x="1067" y="419" text-anchor="middle">BRAMBLETOYS</text>
      <text class="back-copy">
        <tspan x="933" y="474" textLength="262" lengthAdjust="spacing">Our patented design is lightyears ahead</tspan>
        <tspan x="933" y="490" textLength="262" lengthAdjust="spacing">of the competition. This sleek design</tspan>
        <tspan x="933" y="505" textLength="262" lengthAdjust="spacing">means flawless performance and no</tspan>
        <tspan x="933" y="521" textLength="262" lengthAdjust="spacing">downtime (We have less than 1% service</tspan>
        <tspan x="933" y="536" textLength="262" lengthAdjust="spacing">calls, which means these are truly built to</tspan>
        <tspan x="933" y="552" textLength="262" lengthAdjust="spacing">last.) Brambletoys is the most customiz-</tspan>
        <tspan x="933" y="567" textLength="262" lengthAdjust="spacing">able system available, allowing users to</tspan>
        <tspan x="933" y="583" textLength="262" lengthAdjust="spacing">design one-of-a-kind sequences of up to</tspan>
        <tspan x="933" y="598" textLength="262" lengthAdjust="spacing">250 unique color/brightness combina-</tspan>
        <tspan x="1063" y="613" text-anchor="middle">tions at a time.</tspan>
      </text>
      <text class="web-address" x="1063" y="714" text-anchor="middle">WWW.MYBRAMBLETOYS.COM</text>
    </g>

    <!-- bottom end panel -->
    <g class="bottom-end">
      <rect class="frame" x="900" y="764" width="327" height="72"/>
      <path class="frame-thin" d="M919,774 L1208,774 L1218,784 L1218,816 L1208,826 L919,826 L909,816 L909,784 Z"/>
      <text class="pip" x="943" y="806" font-size="14" text-anchor="middle">◆</text>
      <text class="suit suit-heart" x="996" y="807" text-anchor="middle">♥</text>
      <text class="suit suit-club" x="1041" y="807" text-anchor="middle">♣</text>
      <text class="suit suit-diamond" x="1086" y="807" text-anchor="middle">♦</text>
      <text class="suit suit-spade" x="1131" y="807" text-anchor="middle">♠</text>
      <text class="pip" x="1184" y="806" font-size="14" text-anchor="middle">◆</text>
    </g>

    <!-- brand badge -->
    <g class="brand-badge">
      <circle class="badge-disc" cx="1469" cy="320" r="62"/>
      <text class="badge-name" x="1469" y="326" text-anchor="middle">Brambletoys</text>
    </g>
  </svg>
</main>
</body>
</html>
```